Chic streamline modern edgy! Danemerecurls.com

I need a website built for my personal business. I am a hair stylist and I would like a crisp website that works well, is sleek, easy to use, and allows my clients to navigate through Services and pay deposits for services listed.

My logo is somewhat of a full moon, so my theme is nocturnal.

My information can be found at chairbook.com/danemerecurls

Target Market(s)

Women ages 25-55 who are looking for luxury hair extension services

Industry/Entity Type

Hair And Beauty

Number of Pages Required

1 page

Colors
474747
919191
d3d3d3
000000

Requirements
Must have
• Location map, coinvale link embedded for deposits, contact box, bio, faq/policies, menu of services, hours of availability by appointment only .
Nice to have
• An interactive calander where I could post dates that I am available, preferred providers for other beauty services where i could list other websites for make up and other beauty related referrals. a bridal tab would be nice to offer information about bridal services and policies.

```html
<!DOCTYPE html>
<html lang="en">
<head>
<meta charset="utf-8">
<title>Danemere Curls</title>
<link href="https://fonts.googleapis.com/css2?family=Roboto+Condensed:wght@300;400;700&family=Roboto:wght@300;400;500&display=swap" rel="stylesheet">
<style>
:root{
  --black:#000000;
  --ink:#111111;
  --panel:#1f1f1f;
  --card:#2a2a2a;
  --band:#474747;
  --mid:#919191;
  --light:#d3d3d3;
  --white:#ffffff;
  --red:#d0121a;
}
*{margin:0;padding:0;box-sizing:border-box}
html,body{width:1200px;height:2696px;overflow:hidden;background:var(--ink);color:var(--light);font-family:"Roboto",Arial,sans-serif}
.page{position:relative;width:1200px;height:2696px;background:var(--ink)}

/* hero */
.hero{position:absolute;left:0;top:0;width:1200px;height:980px;background:linear-gradient(180deg,#3a3a3a 0%,#262626 70%,#1c1c1c 100%)}
.hero-photo{position:absolute;left:480px;top:0;width:720px;height:760px;background:radial-gradient(ellipse at 55% 35%,#8e8e8e 0%,#5c5c5c 35%,#303030 70%,#262626 100%)}
.brand{position:absolute;left:96px;top:80px;width:180px;text-align:center;color:var(--white)}
.brand-mark{display:block;margin:0 auto 14px;width:64px;height:64px;border-radius:50%;background:var(--light)}
.brand-name{font-family:"Roboto Condensed",sans-serif;font-weight:400;font-size:30px;letter-spacing:3px;text-transform:uppercase;line-height:1.1}
.main-nav{position:absolute;left:30px;top:500px;font-family:"Roboto Condensed",sans-serif;font-size:17px;color:var(--light)}
.pay-badge{position:absolute;right:40px;top:596px;display:flex;align-items:center;gap:6px;font-size:13px;color:var(--light)}
.pay-badge i{width:12px;height:12px;background:var(--mid);display:block}
.bio{position:absolute;left:0;top:760px;width:1200px;height:200px;background:var(--light);color:#333}
.bio-photo{position:absolute;left:80px;top:-40px;width:220px;height:240px;background:radial-gradient(ellipse at 50% 40%,#5a5a5a 0%,#2c2c2c 60%,#1a1a1a 100%)}
.bio h2{position:absolute;left:328px;top:36px;font-family:"Roboto Condensed",sans-serif;font-weight:400;font-size:22px;color:#222}
.bio p{position:absolute;left:328px;top:72px;width:640px;font-size:12px;line-height:16px;color:#444}

/* section headings */
.section-title{position:absolute;left:60px;font-family:"Roboto Condensed",sans-serif;font-weight:400;font-size:30px;color:var(--white);display:flex;align-items:center;gap:10px}
.section-title::before{content:"";width:8px;height:30px;background:var(--mid)}
.section-rule{position:absolute;left:60px;width:1080px;height:1px;background:var(--band)}

/* contact */
.hours{position:absolute;left:60px;top:1090px;font-size:13px;color:var(--light);line-height:20px}
.hours h3{font-size:13px;font-weight:500;color:var(--white);margin-bottom:4px}
.hours td{padding-right:18px}
.map{position:absolute;left:380px;top:1040px;width:380px;height:200px;background:linear-gradient(135deg,#e6e4df 0%,#d6d3cc 100%)}
.calendar{position:absolute;left:830px;top:1040px;width:300px}
.cal-head{font-size:14px;color:var(--light);text-align:center;letter-spacing:1px;margin-bottom:8px}
.cal-grid{display:grid;grid-template-columns:repeat(7,1fr);gap:6px}
.cal-grid span{height:30px;border-radius:50%;background:#333;color:var(--light);font-size:11px;display:flex;align-items:center;justify-content:center}
.cal-grid span.open{background:var(--red);color:var(--white)}
.cal-grid span.dow{background:none;border-radius:0;height:16px;color:var(--mid)}
.cal-note{margin-top:8px;font-size:10px;color:var(--mid);display:flex;align-items:center;gap:6px}
.cal-note i{width:8px;height:8px;background:var(--red);display:block}

/* services */
.group-label{position:absolute;font-size:11px;letter-spacing:1px;color:var(--light);text-transform:uppercase}
.service{position:absolute;width:340px;height:300px;background:var(--card);padding:24px 26px}
.service.short{height:236px}
.service h3{font-weight:400;font-size:24px;color:var(--white);margin-bottom:10px}
.service .desc{font-size:11px;line-height:15px;color:var(--mid);height:60px}
.service .price{position:absolute;left:26px;bottom:26px;font-size:24px;color:var(--white);line-height:28px}
.service .price small{display:block;font-size:22px}
.request{position:absolute;right:22px;bottom:26px;background:var(--red);color:var(--white);font-size:14px;font-weight:500;padding:8px 14px;letter-spacing:.5px}

/* testimonial */
.testimonial{position:absolute;left:0;top:2400px;width:1200px;height:200px;background:#2b2b2b}
.testimonial h4{position:absolute;left:330px;top:52px;font-weight:400;font-size:34px;color:var(--light)}
.testimonial .date{position:absolute;left:520px;top:130px;font-size:14px;color:var(--mid)}
.testimonial blockquote{position:absolute;left:600px;top:50px;width:420px;font-size:14px;line-height:20px;color:var(--mid)}

/* footer */
.footer{position:absolute;left:0;top:2600px;width:1200px;height:96px;background:#151515}
.footer-nav{position:absolute;left:40px;top:30px;font-family:"Roboto Condensed",sans-serif;font-size:16px;color:var(--white)}
.footer-line{position:absolute;left:40px;top:66px;font-size:11px;color:var(--mid)}
.footer-copy{position:absolute;right:40px;top:66px;font-size:11px;color:var(--mid)}
.social{position:absolute;right:40px;top:14px;display:flex;gap:12px}
.social i{width:40px;height:40px;border-radius:50%;background:var(--band);display:block}
</style>
</head>
<body>
<div class="page">

<header class="hero">
  <div class="hero-photo" role="img" aria-label="Black and white portrait of a woman with long straight hair"></div>
  <div class="brand"><span class="brand-mark"></span><div class="brand-name">Danemere<br>Curls</div></div>
  <nav class="main-nav">Contact and Biography | Calendar | Services and Book an Appointment | FAQ</nav>
  <div class="pay-badge"><i></i>coinvale</div>
  <section class="bio">
    <div class="bio-photo" role="img" aria-label="Portrait of the stylist"></div>
    <h2>Biography</h2>
    <p>Professional hair stylist Danemere has devoted a decade to luxury curls, colour and extensions. Trained in salon craft and finishing, she builds every look around the client, her lifestyle and the health of her hair. Her studio is calm, private and by appointment only, so each visit feels personal. From first consultation to final style, every detail is shaped with care, patience and a love for the work.</p>
  </section>
</header>

<h2 class="section-title" style="top:1000px">Contact</h2>
<div class="section-rule" style="top:1036px"></div>
<div class="hours">
  <h3>Business Hours</h3>
  <table>
    <tr><td>Tuesday</td><td>11:00am</td><td>—</td><td>7:00pm</td></tr>
    <tr><td>Wednesday</td><td>11:00am</td><td>—</td><td>7:00pm</td></tr>
    <tr><td>Thursday</td><td>11:00am</td><td>—</td><td>7:00pm</td></tr>
    <tr><td>Friday</td><td>11:00am</td><td>—</td><td>7:00pm</td></tr>
    <tr><td>Saturday</td><td>11:00am</td><td>—</td><td>7:00pm</td></tr>
  </table>
</div>
<div class="map" role="img" aria-label="Street map showing the studio location"></div>
<div class="calendar">
  <div class="cal-head">APRIL 2014</div>
  <div class="cal-grid">
    <span class="dow">S</span><span class="dow">M</span><span class="dow">T</span><span class="dow">W</span><span class="dow">T</span><span class="dow">F</span><span class="dow">S</span>
    <span>30</span><span>31</span><span class="open">1</span><span class="open">2</span><span>3</span><span class="open">4</span><span class="open">5</span>
    <span>6</span><span>7</span><span class="open">8</span><span>9</span><span class="open">10</span><span class="open">11</span><span class="open">12</span>
    <span>13</span><span>14</span><span class="open">15</span><span class="open">16</span><span class="open">17</span><span>18</span><span class="open">19</span>
    <span>20</span><span>21</span><span class="open">22</span><span class="open">23</span><span>24</span><span class="open">25</span><span class="open">26</span>
    <span>27</span><span>28</span><span class="open">29</span><span class="open">30</span><span>1</span><span>2</span><span>3</span>
  </div>
  <div class="cal-note"><i></i>Available dates</div>
</div>

<h2 class="section-title" style="top:1290px">Services and Book an Appointment</h2>
<div class="section-rule" style="top:1326px"></div>

<span class="group-label" style="left:80px;top:1362px">Adjustments</span>
<span class="group-label" style="left:800px;top:1362px">Arrangements</span>
<article class="service" style="left:80px;top:1390px"><h3>Relaxer</h3><p class="desc">For curly clients who want a smooth, soft finish with lasting body.</p><div class="price">$100 and up<small>2 hr.</small></div><span class="request">REQUEST</span></article>
<article class="service" style="left:440px;top:1390px"><h3>Extension removal</h3><p class="desc">Gentle removal of wefts, clean wash and scalp care to follow.</p><div class="price">$85 and up<small>1 hr., 45 min.</small></div><span class="request">REQUEST</span></article>
<article class="service" style="left:800px;top:1390px"><h3>Consultation</h3><p class="desc">Required before any new service so we plan the right look.</p><div class="price">$55<small>15 min.</small></div><span class="request">REQUEST</span></article>

<span class="group-label" style="left:80px;top:1734px">Attachments</span>
<span class="group-label" style="left:440px;top:1734px">Enhancements</span>
<span class="group-label" style="left:800px;top:1734px">Upgrades</span>
<article class="service" style="left:80px;top:1762px"><h3>Extensions</h3><p class="desc">Custom sewn or tape extensions, blended by hand for your texture.</p><div class="price">$275 and up<small>3 hr.</small></div><span class="request">REQUEST</span></article>
<article class="service" style="left:440px;top:1762px"><h3>Color services</h3><p class="desc">Single process, highlights and gloss, tested first for best results.</p><div class="price">$125 and up<small>2 hr.</small></div><span class="request">REQUEST</span></article>
<article class="service" style="left:800px;top:1762px"><h3>Extension Straightening</h3><p class="desc">Smooth finishing for installed extensions with heat protection.</p><div class="price">$50 and up<small>45 min.</small></div><span class="request">REQUEST</span></article>

<article class="service short" style="left:80px;top:2120px"><h3>Hair Cut</h3><p class="desc">Shaping and trim for healthy ends, finished with a style.</p><div class="price">$35 and up<small>45 min.</small></div><span class="request">REQUEST</span></article>
<article class="service short" style="left:440px;top:2120px"><h3>Specialty Curls</h3><p class="desc">Wand curls</p><div class="price">$25 and up<small>1 hr.</small></div><span class="request">REQUEST</span></article>
<article class="service short" style="left:800px;top:2120px"><h3>specialty styles</h3><p class="desc">Updo styling ideal for special events.</p><div class="price">$55 and up<small>45 min.</small></div><span class="request">REQUEST</span></article>

<section class="testimonial">
  <h4>Marisol T.</h4>
  <span class="date">7/08/15</span>
  <blockquote>“I will not let anyone else do my hair but Danemere... Her styling foundation is everything!!! She is so sweet and you are truly entertained in the shop. I love Danemere Curls! Definitely book your next appointment here!”</blockquote>
</section>

<footer class="footer">
  <nav class="footer-nav">HOME | Contact and Biography | Calendar | Services and Book an Appointment | FAQ</nav>
  <div class="social"><i></i><i></i><i></i></div>
  <div class="footer-line">Address: 1200 Larkspur Ave, Suite 4, Oakland · 555-0142</div>
  <div class="footer-copy">© 2014 Danemerecurls.com  All rights reserved.</div>
</footer>

</div>
</body>
</html>
```